Brisa Lumen Systems Corp Business Cards

Business cards to match the logo.

Company is a start up water technology company that has developed a patented system using centrifugal force to separate waste from municipal waste water to produce crystal clear clean water. Product sell starting at 2 million to governments both in the US and international.

Business cards should have a professional look with the target generally engineers.

Target Market(s)

Engineers, Government officials and investors

Industry/Entity Type

Water Treatment

Contact Information for Business Card

Business cards design will be used for 6 to 8 people with job titles. Can use the quote "If there is magic in the planet, it is contained in water." but not required to use quote. Should follow theme of Logo

Font styles to use
Other font styles liked:
• match logo font

Requirements
Nice to have
• Colors to match Logo. Business cards to match style of flow of Logo.
• Emphasis on clean look not a busy look. Clean flowing water.
Should not have
• Pictures of industrial equipment or wastewater

```html
<!DOCTYPE html>
<html lang="en">
<head>
<meta charset="utf-8">
<title>Brisa Lumen Systems Corp – Business Cards</title>
<link href="https://fonts.googleapis.com/css2?family=EB+Garamond:wght@400;500;600&display=swap" rel="stylesheet">
<style>
  :root {
    --ink-deep: #0b5078;
    --water-bright: #2aa6e0;
    --paper: #ffffff;
    --backdrop: #e9e9e9;
    --text-dark: #2b2b2b;
  }
  * { box-sizing: border-box; margin: 0; padding: 0; }
  html, body {
    width: 1200px; height: 586px; overflow: hidden;
    background: var(--backdrop);
    font-family: "EB Garamond", Georgia, serif;
  }
  .canvas { position: relative; width: 1200px; height: 586px; }
  .card {
    position: absolute; top: 129px; width: 501px; height: 300px; overflow: hidden;
  }
  .card--front { left: 61px; background: var(--ink-deep); }
  .card--back { left: 619px; background: var(--paper); }

  .wordmark { position: absolute; font-weight: 400; text-align: center; line-height: 1; }
  .wordmark__name { display: block; letter-spacing: 0.01em; }
  .wordmark__tag { display: block; }

  .card--front .wordmark {
    left: 0; right: 0; top: 128px; color: var(--paper);
  }
  .card--front .wordmark__name { font-size: 52px; }
  .card--front .wordmark__tag { font-size: 25px; letter-spacing: 0.42em; margin-top: 6px; padding-left: 0.42em; }

  .card--back .wordmark {
    left: 252px; width: 220px; top: 70px; color: var(--ink-deep);
  }
  .card--back .wordmark__name { font-size: 33px; }
  .card--back .wordmark__tag { font-size: 16px; letter-spacing: 0.42em; margin-top: 3px; padding-left: 0.42em; }

  .holder { position: absolute; left: 37px; top: 42px; }
  .holder__name { font-size: 19px; font-weight: 600; color: var(--ink-deep); }
  .holder__title { font-size: 12.5px; color: var(--text-dark); margin-top: 1px; }

  .waves { position: absolute; left: 0; top: 0; width: 501px; height: 300px; }

  .contacts { position: absolute; left: 37px; top: 190px; list-style: none; color: var(--paper); }
  .contacts li { display: flex; align-items: center; height: 22px; font-size: 12.5px; }
  .contacts .icon {
    width: 17px; height: 17px; border-radius: 50%; background: var(--paper);
    margin-right: 9px; display: flex; align-items: center; justify-content: center;
  }
  .contacts .icon svg { width: 11px; height: 11px; }
  .address {
    position: absolute; left: 37px; top: 258px; color: var(--paper);
    font-size: 15.5px; font-weight: 600;
  }
</style>
</head>
<body>
<main class="canvas">
  <section class="card card--front" aria-label="Card front">
    <div class="wordmark">
      <span class="wordmark__name">BRISA LUMEN</span>
      <span class="wordmark__tag">SYSTEMS</span>
    </div>
  </section>

  <section class="card card--back" aria-label="Card back">
    <svg class="waves" viewBox="0 0 501 300" aria-hidden="true">
      <path d="M0 128 C 70 108, 160 122, 255 168 S 420 248, 501 220 L501 300 L0 300 Z" fill="var(--water-bright)"/>
      <path d="M0 141 C 70 122, 160 138, 255 184 S 420 262, 501 232 L501 300 L0 300 Z" fill="var(--ink-deep)"/>
    </svg>

    <div class="holder">
      <p class="holder__name">Marisol Pennington</p>
      <p class="holder__title">Owner / Founder</p>
    </div>

    <div class="wordmark">
      <span class="wordmark__name">BRISA LUMEN</span>
      <span class="wordmark__tag">SYSTEMS</span>
    </div>

    <ul class="contacts">
      <li><span class="icon"><svg viewBox="0 0 12 12"><path d="M2 4 Q6 1 10 4 L9 5.5 L7.5 4.8 L7.5 4 Q6 3.6 4.5 4 L4.5 4.8 L3 5.5 Z M3 7 H9 V10 H3 Z" fill="var(--ink-deep)"/></svg></span>+612 5550 1482</li>
      <li><span class="icon"><svg viewBox="0 0 12 12"><rect x="3.5" y="1.5" width="5" height="3" fill="var(--ink-deep)"/><rect x="1.5" y="4.5" width="9" height="4" rx="1" fill="var(--ink-deep)"/><rect x="3.5" y="7.5" width="5" height="3" fill="var(--ink-deep)"/></svg></span>+612 5550 1497</li>
      <li><span class="icon"><svg viewBox="0 0 12 12"><rect x="1.5" y="3" width="9" height="6" fill="none" stroke="var(--ink-deep)" stroke-width="1.2"/><path d="M1.5 3 L6 6.5 L10.5 3" fill="none" stroke="var(--ink-deep)" stroke-width="1.2"/></svg></span>info@brisalumen.com</li>
    </ul>
    <p class="address">41-12 58th Pl, Harbor Point NY 11420</p>
  </section>
</main>
</body>
</html>
```